Membership Card Design

I need a basic membership card...it will entitle the customer to free entry to forthcoming promotions.
The business is called STARLANE PLAY and is a amusement arcade located in N Ireland.
I require .....
STARLANE PLAY MEMBER...across top of card in logo format.
Next line....this card entitles the holder free entry to forthcoming STARLANE EVENTS....
Then next line....customer name( space to write their name )
Next line.....customer mobile number ( space to write number )
On rear of card....logo/picture & STARLANE PLAY MEMBER written on back.

Industry/Entity Type

Business

Contact Information for Business Card

STARLANE PLAY
MEMBERSHIP CARD

```html
<!DOCTYPE html>
<html lang="en">
<head>
<meta charset="utf-8">
<title>Starlane Play Membership Card</title>
<link rel="stylesheet" href="https://fonts.googleapis.com/css2?family=Bebas+Neue&display=swap">
<style>
  :root {
    --ink-black: #050505;
    --panel-dark: #0d0d0d;
    --panel-mid: #1a1a1a;
    --silver-light: #f4f4f4;
    --silver-mid: #c9c9c9;
    --silver-dark: #8a8a8a;
    --rule-glow: rgba(235, 235, 235, 0.85);
  }
  * { box-sizing: border-box; margin: 0; padding: 0; }
  html, body {
    width: 910px;
    height: 1200px;
    overflow: hidden;
    background: var(--ink-black);
  }
  .sheet {
    position: relative;
    width: 910px;
    height: 1200px;
    font-family: "Bebas Neue", "Oswald", sans-serif;
    text-align: center;
  }
  .card-face {
    position: absolute;
    left: 0;
    width: 910px;
    height: 600px;
    background:
      repeating-linear-gradient(180deg, rgba(255,255,255,0.018) 0 1px, transparent 1px 4px),
      radial-gradient(ellipse 70% 55% at 50% 30%, var(--panel-mid), var(--panel-dark) 60%, var(--ink-black));
  }
  .card-face--front { top: 0; }
  .card-face--back { top: 600px; }

  .brand-name {
    position: absolute;
    left: 0;
    right: 0;
    font-size: 84px;
    line-height: 1;
    letter-spacing: 2px;
    color: var(--silver-mid);
  }
  .card-face--front .brand-name { top: 110px; }
  .card-face--back .brand-name { top: 146px; }

  .metal-text {
    background: linear-gradient(180deg, var(--silver-light) 0%, var(--silver-mid) 55%, var(--silver-dark) 100%);
    -webkit-background-clip: text;
    background-clip: text;
    color: transparent;
  }

  .entitlement {
    position: absolute;
    top: 280px;
    left: 0;
    right: 0;
    font-size: 31px;
    line-height: 28px;
  }
  .field-label {
    position: absolute;
    left: 0;
    right: 0;
    line-height: 1;
  }
  .field-label--name { top: 340px; font-size: 52px; }
  .field-label--mobile { top: 443px; font-size: 44px; }

  .write-rule {
    position: absolute;
    left: 215px;
    width: 460px;
    height: 2px;
    background: linear-gradient(90deg, transparent, var(--rule-glow) 30%, var(--rule-glow) 70%, transparent);
  }
  .write-rule--name { top: 435px; }
  .write-rule--mobile { top: 548px; }

  .member-title {
    position: absolute;
    top: 330px;
    left: 0;
    right: 0;
    font-size: 80px;
    line-height: 1;
    letter-spacing: 1px;
  }
</style>
</head>
<body>
  <main class="sheet">
    <section class="card-face card-face--front" aria-label="Card front">
      <div class="brand-name">STARLANE PLAY</div>
      <p class="entitlement metal-text">This card entitles the holder free<br>entry to forthcoming STARLANE EVENTS</p>
      <p class="field-label field-label--name metal-text">CUSTOMER NAME</p>
      <div class="write-rule write-rule--name"></div>
      <p class="field-label field-label--mobile metal-text">CUSTOMER MOBILE NUMBER</p>
      <div class="write-rule write-rule--mobile"></div>
    </section>

    <section class="card-face card-face--back" aria-label="Card back">
      <div class="brand-name">STARLANE PLAY</div>
      <h1 class="member-title metal-text">STARLANE PLAY MEMBER</h1>
    </section>
  </main>
</body>
</html>
```